Creative & Professional Business Card for hair salon

We are looking to update our business cards. Our salon is creative, modern, progressive and professional and looking for a design that will reflect this.

```html
<!DOCTYPE html>
<html lang="en">
<head>
<meta charset="utf-8">
<title>Skyline Hair Studio – Business Card</title>
<link rel="stylesheet" href="https://fonts.googleapis.com/css2?family=Quicksand:wght@400&family=Arimo:wght@400&family=Tinos:wght@400&display=swap">
<style>
  :root {
    --backdrop: #2b2b2b;
    --sky-deep: #2f86d3;
    --sky-mid: #6fb3ea;
    --sky-light: #cfe6f8;
    --glow: #ffffff;
    --band-edge: #3d93dc;
    --band-main: #3a8bd4;
    --stripe: #f4f8fc;
    --logo-ink: #4d8fae;
    --card-text: #ffffff;
    --appt-ink: #e9f3fc;
    --line-ink: #1f5f99;
  }
  * { box-sizing: border-box; margin: 0; padding: 0; }
  html, body {
    width: 1200px; height: 997px; overflow: hidden;
    background: var(--backdrop);
  }
  .canvas { position: relative; width: 1200px; height: 997px; }
  .card {
    position: absolute; left: 280px;
    width: 640px; height: 390px;
    overflow: hidden; border-radius: 3px;
    box-shadow: 0 8px 24px rgba(0,0,0,.45);
  }
  .card--appointment { top: 70px; }
  .card--contact { top: 530px; }

  .sky {
    position: absolute; inset: 0;
    background:
      radial-gradient(ellipse 45% 55% at 38% 18%, var(--glow) 0%, rgba(255,255,255,.6) 35%, rgba(255,255,255,0) 75%),
      linear-gradient(160deg, var(--sky-light) 0%, var(--sky-mid) 45%, var(--sky-deep) 100%);
  }
  .wave { position: absolute; inset: 0; width: 640px; height: 390px; }

  .logo {
    position: absolute;
    font-family: "Quicksand", sans-serif; font-weight: 400;
    color: var(--logo-ink);
    text-align: center;
  }
  .logo__name { font-size: 30px; letter-spacing: .5px; display: block; }
  .logo__by { font-size: 15px; display: block; margin-top: 2px; }
  .card--appointment .logo { left: 36px; top: 80px; text-align: left; }
  .card--contact .logo { left: 0; right: 0; top: 70px; }

  .appointment {
    position: absolute; left: 345px; top: 190px; width: 275px;
    font-family: "Tinos", serif; color: var(--appt-ink);
  }
  .appointment__title {
    font-size: 20px; letter-spacing: 3px; text-transform: uppercase;
    white-space: nowrap;
    margin-bottom: 30px;
  }
  .appointment__field {
    font-size: 16px; color: var(--line-ink);
    display: flex; align-items: baseline; gap: 8px; margin-bottom: 24px;
  }
  .appointment__line {
    flex: 1; border-bottom: 2px dotted var(--line-ink); height: 1px;
  }

  .contact {
    position: absolute; left: 36px; top: 278px;
    list-style: none;
    font-family: "Arimo", sans-serif; font-size: 18px;
    color: var(--card-text);
  }
  .contact__item {
    display: flex; align-items: center; gap: 10px; height: 25px;
  }
  .contact__icon { width: 16px; height: 16px; flex: none; }
</style>
</head>
<body>
<main class="canvas">

  <section class="card card--appointment" aria-label="Appointment card">
    <div class="sky" role="img" aria-label="Blue sky photograph with sun rays and white clouds"></div>
    <svg class="wave" viewBox="0 0 640 390" aria-hidden="true">
      <path d="M40,390 C200,380 220,60 640,30 L640,390 Z" fill="var(--band-edge)"/>
      <path d="M66,390 C226,382 246,76 640,48 L640,390 Z" fill="var(--stripe)"/>
      <path d="M92,390 C252,384 272,92 640,64 L640,390 Z" fill="var(--band-main)"/>
    </svg>
    <div class="logo">
      <span class="logo__name">Skyline Hair Studio</span>
      <span class="logo__by">by Lena Marsh</span>
    </div>
    <div class="appointment">
      <p class="appointment__title">Next Appointment</p>
      <p class="appointment__field">Time: <span class="appointment__line"></span></p>
      <p class="appointment__field">Date: <span class="appointment__line"></span></p>
    </div>
  </section>

  <section class="card card--contact" aria-label="Contact card">
    <div class="sky" role="img" aria-label="Blue sky photograph with sun rays and white clouds"></div>
    <svg class="wave" viewBox="0 0 640 390" aria-hidden="true">
      <path d="M0,228 C150,205 260,248 400,232 S560,190 640,168 L640,390 L0,390 Z" fill="var(--band-edge)"/>
      <path d="M0,240 C150,217 260,260 400,244 S560,202 640,180 L640,390 L0,390 Z" fill="var(--stripe)"/>
      <path d="M0,252 C150,229 260,272 400,256 S560,214 640,192 L640,390 L0,390 Z" fill="var(--band-main)"/>
    </svg>
    <div class="logo">
      <span class="logo__name">Skyline Hair Studio</span>
      <span class="logo__by">by Lena Marsh</span>
    </div>
    <ul class="contact">
      <li class="contact__item">
        <svg class="contact__icon" viewBox="0 0 16 16" aria-hidden="true"><circle cx="8" cy="8" r="8" fill="#fff"/><path d="M5,4 L7,4 L7.5,6 L6.5,7 C7,8.2 7.8,9 9,9.5 L10,8.5 L12,9 L12,11 C8,11.5 4.5,8 5,4 Z" fill="var(--band-main)"/></svg>
        07 5500 0123
      </li>
      <li class="contact__item">
        <svg class="contact__icon" viewBox="0 0 16 16" aria-hidden="true"><circle cx="8" cy="8" r="8" fill="#fff"/><rect x="4" y="5" width="8" height="6" fill="none" stroke="var(--band-main)" stroke-width="1.2"/><path d="M4,5 L8,8.5 L12,5" fill="none" stroke="var(--band-main)" stroke-width="1.2"/></svg>
        salon@skylinehairstudio.com.au
      </li>
      <li class="contact__item">
        <svg class="contact__icon" viewBox="0 0 16 16" aria-hidden="true"><circle cx="8" cy="8" r="8" fill="#fff"/><circle cx="8" cy="8" r="4" fill="none" stroke="var(--band-main)" stroke-width="1.1"/><ellipse cx="8" cy="8" rx="1.8" ry="4" fill="none" stroke="var(--band-main)" stroke-width="1"/><path d="M4,8 L12,8" stroke="var(--band-main)" stroke-width="1"/></svg>
        skylinehairbylenamarsh
      </li>
      <li class="contact__item">
        <svg class="contact__icon" viewBox="0 0 16 16" aria-hidden="true"><circle cx="8" cy="8" r="8" fill="#fff"/><path d="M8,13 C6,10 5,8.5 5,7 A3,3 0 0 1 11,7 C11,8.5 10,10 8,13 Z" fill="var(--band-main)"/><circle cx="8" cy="7" r="1.1" fill="#fff"/></svg>
        3/12 Harbour Road, Coolum Qld 4573
      </li>
    </ul>
  </section>

</main>
</body>
</html>
```